Wine labels Velmora Wine Council - Nueva etiqueta El Consejo Regulador de vinos de Albarrán

Velmora Wines Council, based in southern Spain, are looking to create a new suite of wine labels which retain the elegance of the Velmora Wines industry while reinvigorating their image to the modern era and a new generation of Sherry Wine lovers. These labels will be used across the Velmora Wines Council's range of wines for the promotion of the Velmora Wines industry.

Your design must present at least two styles of Velmora Wines which demonstrate an elegant, modern interpretation and understanding of the unique mood and personality for these wines and the essence of southern Spain.

10 labels will be created based on the winning design, one for each of the unique varieties of Velmora Wines within the collection. This collection comprises of several different wine varieties including: Fino, Manzanilla, Amontillado, Oloroso, Palo Cortado, Medium, Cream, Pale Cream, Pedro Ximenez and Moscatel.

We recommend you visit our website www.velmora-vinos.example/wines as the source to understanding the origins and unique personality of these diverse wines.

El Consejo Regulador de los Vinos de Albarrán y Tordesal quiere renovar las etiquetas de los vinos utilizados para sus actividades de promoción genérica. Esta colección de vinos comprende las tipologías más importantes de la región que incluye: fino, manzanilla, amontillado, oloroso, palo cortado, pale cream, medium, cream, pedro ximénez y moscatel. Por lo tanto se precisan 10 etiquetas, una para cada uno de los vinos mencionados.
Updates

Project Deadline Extended
Reason: Due to some confusion with the deadline we wish to officially extend the deadline to allow designers one last week to submit their entries.

Target Market(s)

Industry, journalists, media, sommeliers, chefs, wine writers

Industry/Entity Type

Council

Requirements
Must have
• Front and Back label plus capsule:
• Front label can have either of the two official logos of the Velmora Wine council titled Vinos de Albarrán Digital or not, this is optional. Must include: Vino selecionado por el Consejo Regulador de la Denominacion de Origen, Name of the variety of wine eg FINO, percentage of alcohol eg 15% and quantity 75 cl.
• The back of the label must include the council logo titled Sellora and 4 additional logos positioned smaller. The Europa logo must appear larger than the 3 other logos. Space for descriptive text about the wine is also required.
• The dimensions of the bottle can be found at this link http://www.vidrialto.example/es/catalogo/vinos-y-espumosos/bordelesas/bd-orla
• Altura:305 mm
• Diámetro base:76,20 mm
• Diámetro hombro:82 mm
• Tipo boca:Cetie
• Peso:750 gr
• Capacidad:75 cl
• Etiqueta delantera y trasera y capsula
• La etiqueta delantera puede incluir el logo oficial del Consejo Regulador o el logo digital, o ninguno, esto es opcional. Debe incluir el siguiete texto: Vino selecionado por el Consejo Regulador de la Denominacion de Origen, el nombre de la variedad del vino, por ejemplo Fino, el porcentaje de alcohol, por ejemplo 15%, y la capacidad 75cl.
• La etiqueta trasera debe incluir el logo oficial Sellora del Consejo, y cuatro logos adicionales con una dimension menor. El Logo de ¨Europa invierte en las zonas rurales¨ debe ser de mayor tamaño que los otros. Se precisa espacio para el texto descriptivo de los vinos.
• Las dimensiones de la botella se puede encontrar en este enlace
• http://www.vidrialto.example/es/catalogo/vinos-y-espumosos/bordelesas/bd-orla
• Altura:305 mm
• Diámetro base:76,20 mm
• Diámetro hombro:82 mm
• Tipo boca:Cetie
• Peso:750 gr
• Capacidad:75 cl
Nice to have
• See our website velmora-vinos.example to understand the origin of the wines. Ver nuestra página web velmora-vinos.example para mejor entender los vinos.
Should not have
• Images of catavinos or stereotypical images from Spain such as flamenco dancers or guitars.

```html
<!DOCTYPE html>
<html lang="es">
<head>
<meta charset="utf-8">
<title>Vinos de Albarrán — etiquetas</title>
<link href="https://fonts.googleapis.com/css2?family=Cormorant+Garamond:wght@500;600&family=Montserrat:wght@500;700&display=swap" rel="stylesheet">
<style>
  :root{
    --page:#ffffff;
    --gold:#c9a25a;
    --gold-light:#e6cc8e;
    --gold-dark:#9c7a3c;
    --amontillado-top:#7a3a1f;
    --amontillado-bottom:#4d2312;
    --manzanilla-top:#f6eed3;
    --manzanilla-bottom:#eadcae;
    --cream-top:#4a1a14;
    --cream-bottom:#2a0c09;
    --ink-light:#f4ead6;
    --ink-dark:#3a1a10;
  }
  *{box-sizing:border-box;margin:0;padding:0}
  html,body{width:1200px;height:900px;overflow:hidden;background:var(--page)}
  .collection{
    position:relative;width:1200px;height:900px;
    display:flex;justify-content:center;align-items:center;gap:44px;
  }
  .label{
    position:relative;width:300px;height:560px;
    display:flex;flex-direction:column;align-items:center;
    padding:34px 18px 0;
    box-shadow:0 10px 30px rgba(0,0,0,.18);
  }
  .label--amontillado{background:linear-gradient(180deg,var(--amontillado-top),var(--amontillado-bottom));color:var(--ink-light)}
  .label--manzanilla{background:linear-gradient(180deg,var(--manzanilla-top),var(--manzanilla-bottom));color:var(--ink-dark)}
  .label--cream{background:linear-gradient(180deg,var(--cream-top),var(--cream-bottom));color:var(--ink-light)}
  .label::before{content:"";position:absolute;inset:6px;border:1px solid var(--gold);opacity:.55;pointer-events:none}

  .brand{display:flex;flex-direction:column;align-items:center;gap:6px;margin-top:6px}
  .brand__mark{width:12px;height:12px;border-radius:50%;border:1.5px solid var(--gold)}
  .brand__name{font-family:"Cormorant Garamond",serif;font-weight:500;font-size:23px;letter-spacing:.5px;color:inherit;white-space:nowrap}
  .brand__sub{font-family:"Montserrat",sans-serif;font-weight:500;font-size:8px;letter-spacing:3px;text-transform:uppercase;opacity:.8}

  .variety{position:relative;width:100%;height:110px;margin-top:14px;display:flex;align-items:center;justify-content:center}
  .variety__initial{font-family:"Cormorant Garamond",serif;font-weight:500;font-size:118px;line-height:1;color:var(--gold)}
  .variety__name{position:absolute;top:50%;left:0;right:0;transform:translateY(-50%);text-align:center;
    font-family:"Montserrat",sans-serif;font-weight:700;font-size:17px;letter-spacing:5px;text-transform:uppercase}
  .label--manzanilla .variety__name{color:var(--ink-dark)}
  .label--amontillado .variety__name,.label--cream .variety__name{color:var(--ink-light)}

  .statement{font-family:"Montserrat",sans-serif;font-weight:700;font-size:7.5px;line-height:1.4;text-align:center;text-transform:uppercase;letter-spacing:.3px;margin-top:6px}

  .scene{width:calc(100% + 36px);height:190px;margin-top:14px}
  .scene--amontillado{background:linear-gradient(180deg,#5a2a16 0%,#3b1c10 45%,#6b4a36 100%)}
  .scene--manzanilla{background:linear-gradient(180deg,#e9dcc0 0%,#8a4a3a 35%,#5a2a22 100%)}
  .scene--cream{background:linear-gradient(180deg,#3a1410 0%,#5a3a32 50%,#8a7a70 100%)}

  .footer{width:calc(100% + 36px);margin-top:auto;margin-bottom:14px;padding:8px 16px;
    border-top:2px solid var(--gold);border-bottom:2px solid var(--gold);
    display:flex;justify-content:space-between;align-items:center;
    font-family:"Montserrat",sans-serif;font-size:9px;letter-spacing:1.5px;text-transform:uppercase}
  .footer__volume,.footer__abv{font-weight:500;color:var(--gold)}
  .footer__house{font-weight:700;text-align:center;line-height:1.35}
  .label--manzanilla .footer{background:linear-gradient(90deg,var(--gold-dark),var(--gold-light),var(--gold-dark));color:var(--ink-dark)}
  .label--manzanilla .footer__volume,.label--manzanilla .footer__abv{color:var(--ink-dark)}
  .label--amontillado .footer,.label--cream .footer{color:var(--gold-light)}
</style>
</head>
<body>
<main class="collection">

  <article class="label label--amontillado">
    <div class="brand"><span class="brand__mark"></span><span class="brand__name">VINOS DE ALBARRÁN</span><span class="brand__sub">Velmora Wines</span></div>
    <div class="variety"><span class="variety__initial">A</span><span class="variety__name">Amontillado</span></div>
    <p class="statement">Vino selecionado por el Consejo Regulador<br>de la Denominacion de Origen</p>
    <div class="scene scene--amontillado" role="img" aria-label="Grabado de colinas con cipreses y viñedos"></div>
    <div class="footer"><span class="footer__volume">75 cl</span><span class="footer__house">Bodegas Orvieda</span><span class="footer__abv">19% vol</span></div>
  </article>

  <article class="label label--manzanilla">
    <div class="brand"><span class="brand__mark"></span><span class="brand__name">VINOS DE ALBARRÁN</span><span class="brand__sub">Velmora Wines</span></div>
    <div class="variety"><span class="variety__initial">M</span><span class="variety__name">Manzanilla</span></div>
    <p class="statement">Vino selecionado por el Consejo Regulador<br>de la Denominacion de Origen</p>
    <div class="scene scene--manzanilla" role="img" aria-label="Grabado sepia de vendimiadores cargando uva en la viña"></div>
    <div class="footer"><span class="footer__volume">75 cl</span><span class="footer__house">Bodegas Tordesal<br>de Marina</span><span class="footer__abv">19% vol</span></div>
  </article>

  <article class="label label--cream">
    <div class="brand"><span class="brand__mark"></span><span class="brand__name">VINOS DE ALBARRÁN</span><span class="brand__sub">Velmora Wines</span></div>
    <div class="variety"><span class="variety__initial">C</span><span class="variety__name">Cream</span></div>
    <p class="statement">Vino selecionado por el Consejo Regulador<br>de la Denominacion de Origen</p>
    <div class="scene scene--cream" role="img" aria-label="Grabado de hileras de viñedo hasta el horizonte"></div>
    <div class="footer"><span class="footer__volume">75 cl</span><span class="footer__house">Bodegas Orvieda</span><span class="footer__abv">19% vol</span></div>
  </article>

</main>
</body>
</html>
```